Update Business Card Design

I'm looking to update my business cards. Attached is a photo of the current design. I like the black side so that does not have to be update. The white side needs to be updated. I want the design to be modern and minimalistic.
I am a lawyer and my firm's website is www.brennoxlegalco.com (for reference).
My firm's logo has a horizontal version (which is on the black side of the card) and a vertical version (on the white side). I would prefer to keep the vertical version on the white side and horizontal version on the black side (the logo files are attached).

I am open to redesigning the black side also. I would like one side to have the horizontal logo and the other to have the vertical logo.

```html
<!DOCTYPE html>
<html lang="en">
<head>
<meta charset="utf-8">
<title>Brennox Legal Co – Business Cards</title>
<link rel="stylesheet" href="https://fonts.googleapis.com/css2?family=Cormorant+Garamond:wght@500&family=Montserrat:wght@400;500;700&display=swap">
<style>
  :root {
    --bg: #4a4a4a;
    --card-dark: #222222;
    --card-light: #ffffff;
    --brand: #12b5e2;
    --brand-faint: #e4f5fb;
    --ink: #3a3a3a;
    --ink-soft: #555555;
    --white: #ffffff;
  }
  * { box-sizing: border-box; margin: 0; padding: 0; }
  html, body { width: 1200px; height: 875px; overflow: hidden; }
  body {
    background: var(--bg);
    font-family: "Montserrat", sans-serif;
    display: flex;
    flex-direction: column;
    align-items: center;
    justify-content: center;
    gap: 40px;
  }
  .card {
    position: relative;
    width: 620px;
    height: 354px;
    border-radius: 22px;
    overflow: hidden;
    box-shadow: 0 10px 30px rgba(0,0,0,0.35);
  }

  /* Front: horizontal logo */
  .card--front { background: var(--card-dark); }
  .front-logo {
    position: absolute;
    left: 0; right: 0; top: 118px;
    display: flex;
    align-items: center;
    justify-content: center;
    gap: 18px;
  }
  .logo-mark {
    width: 26px; height: 26px;
    background: var(--brand);
  }
  .logo-name {
    font-family: "Cormorant Garamond", serif;
    font-weight: 500;
    color: var(--brand);
    letter-spacing: 2px;
    text-transform: uppercase;
    line-height: 1;
  }
  .front-logo .logo-name { font-size: 50px; }
  .front-web {
    position: absolute;
    left: 0; right: 0; bottom: 70px;
    text-align: center;
    color: var(--white);
    font-size: 15px;
    letter-spacing: 2px;
  }

  /* Back: vertical logo and contact details */
  .card--back { background: var(--card-light); }
  .back-decor {
    position: absolute;
    right: -70px; top: -60px;
  }
  .back-band {
    position: absolute;
    left: 0; bottom: 0;
  }
  .back-logo {
    position: absolute;
    left: 40px; top: 38px;
    display: flex;
    flex-direction: column;
    align-items: flex-start;
    gap: 12px;
  }
  .back-logo .logo-mark { width: 34px; height: 34px; }
  .back-logo .logo-name { font-size: 28px; }
  .back-logo .logo-rule {
    width: 150px; height: 1px; background: var(--ink-soft);
  }
  .holder {
    position: absolute;
    right: 46px; top: 72px;
    text-align: right;
  }
  .holder-name {
    font-weight: 700;
    font-size: 26px;
    color: var(--brand);
    letter-spacing: 1px;
    text-transform: uppercase;
  }
  .holder-title { font-size: 14px; color: var(--ink); margin-top: 2px; }
  .holder-phone { font-size: 18px; color: var(--brand); margin-top: 4px; letter-spacing: 1px; }
  .holder-accent {
    position: absolute;
    right: 0; top: 72px;
    width: 18px; height: 36px;
    background: var(--brand);
  }
  .address {
    position: absolute;
    left: 40px; top: 172px;
    font-size: 13px;
    line-height: 1.45;
    color: var(--ink);
  }
  .contacts {
    position: absolute;
    left: 40px; top: 222px;
    list-style: none;
    font-size: 13px;
    line-height: 1.55;
    color: var(--ink);
  }
  .contacts li { display: flex; align-items: center; gap: 8px; }
  .contacts svg { width: 12px; height: 12px; fill: var(--brand); flex: none; }
</style>
</head>
<body>

  <section class="card card--front" aria-label="Card front">
    <div class="front-logo">
      <span class="logo-mark"></span>
      <span class="logo-name">Brennox Legal Co</span>
    </div>
    <p class="front-web">www.brennoxlegalco.com</p>
  </section>

  <section class="card card--back" aria-label="Card back">
    <svg class="back-decor" width="380" height="380" viewBox="0 0 380 380" aria-hidden="true">
      <circle cx="190" cy="190" r="180" fill="var(--brand-faint)"/>
      <circle cx="190" cy="190" r="110" fill="var(--card-light)"/>
    </svg>
    <svg class="back-band" width="620" height="40" viewBox="0 0 620 40" aria-hidden="true">
      <polygon points="0,28 620,0 620,40 0,40" fill="var(--brand)"/>
    </svg>

    <div class="back-logo">
      <span class="logo-mark"></span>
      <span class="logo-rule"></span>
      <span class="logo-name">Brennox Legal Co</span>
    </div>

    <div class="holder">
      <p class="holder-name">Marcus Hale</p>
      <p class="holder-title">Attorney at Law</p>
      <p class="holder-phone">555.014.2286</p>
    </div>
    <span class="holder-accent"></span>

    <p class="address">1180 Larkmoor Avenue, Suite 304<br>Fairview Heights, CA 90011</p>

    <ul class="contacts">
      <li><svg viewBox="0 0 12 12"><path d="M2.5 0.5l2 2-1 1.5c.6 1.4 1.6 2.4 3 3l1.5-1 2 2-1.5 2C4 11.5 0.5 8 0.5 2z"/></svg>555.014.7710</li>
      <li><svg viewBox="0 0 12 12"><rect x="3" y="0.5" width="6" height="3"/><rect x="0.5" y="4" width="11" height="5" rx="1"/><rect x="3" y="8" width="6" height="3.5"/></svg>555.014.7723</li>
      <li><svg viewBox="0 0 12 12"><path d="M0.5 2h11v8h-11z M0.5 2l5.5 4.5 5.5-4.5" stroke="var(--card-light)" stroke-width="0.8"/></svg>marcus@BrennoxLegalCo.com</li>
      <li><svg viewBox="0 0 12 12"><circle cx="6" cy="6" r="5.5"/><path d="M0.5 6h11M6 0.5v11" stroke="var(--card-light)" stroke-width="0.8"/></svg>www.brennoxlegalco.com</li>
    </ul>
  </section>

</body>
</html>
```